Business Card Design - CPA Firm

Need a Business Card for my CPA Firm. I'd like to include both my favicon (perhaps front) and Logo (perhaps back) on the card.

I'll attach my Brand Template (includes font and color), Logo and Favicon.

I'd like a beach and palm tree image/resemblance in the design.
Updates

Please see additional notes I've added.

Rosalind M. Vantrecourt, CPA
CPA@LedgerhouseofSeagroveShores.example
Servicing Seagrove Coast & Beyond
North Seagrove Shores, SG 00417
(555) 748-2916

Target Market(s)

Small Business Owners, Entrepreneurs and Professions.

Industry/Entity Type

Accounting/ CPA Firm

Contact Information for Business Card

We empower businesses and professionals for success through our strategic accounting solutions!

Requirements
Must have
• Branding: Font, Colors, Logo and Favicon
Nice to have
• For address: Servicing Seagrove Coast & Beyond, North Seagrove Shores, SG 00417
Should not have
• My Physical Street Address (see "Nice to Haves")

```html
<!DOCTYPE html>
<html lang="en">
<head>
<meta charset="utf-8">
<title>Ledgerhouse of Seagrove Shores – Business Card</title>
<link rel="stylesheet" href="https://fonts.googleapis.com/css2?family=Montserrat:wght@400;500;700&display=swap">
<style>
  :root {
    --navy: #22307f;
    --navy-deep: #1d2a72;
    --gold: #f5b820;
    --ink: #2b2b2b;
    --paper: #ffffff;
    --stage: #3a3a3a;
  }
  * { box-sizing: border-box; margin: 0; padding: 0; }
  html, body { width: 1200px; height: 1200px; overflow: hidden; }
  body {
    background: var(--stage);
    font-family: "Montserrat", Arial, sans-serif;
    display: flex;
    flex-direction: column;
    align-items: center;
    justify-content: center;
    gap: 60px;
  }
  .card {
    width: 840px;
    height: 480px;
    border-radius: 34px;
    position: relative;
    overflow: hidden;
  }
  .card-front { background: var(--paper); color: var(--ink); }
  .card-back {
    background: linear-gradient(135deg, #283a8c 0%, var(--navy) 50%, var(--navy-deep) 100%);
    display: flex;
    flex-direction: column;
    align-items: center;
    justify-content: center;
    gap: 28px;
  }

  .brand {
    position: absolute;
    top: 58px;
    left: 0;
    right: 0;
    text-align: center;
  }
  .brand-name {
    font-weight: 700;
    font-size: 34px;
    letter-spacing: 2px;
    text-transform: uppercase;
    color: var(--navy);
    line-height: 1.2;
  }
  .brand-tagline {
    margin-top: 10px;
    font-weight: 500;
    font-size: 13px;
    letter-spacing: 3px;
    text-transform: uppercase;
    color: var(--navy);
  }

  .holder {
    position: absolute;
    left: 56px;
    top: 220px;
  }
  .holder-name {
    font-weight: 700;
    font-size: 30px;
    text-transform: uppercase;
    color: var(--navy);
    letter-spacing: 0.5px;
  }
  .holder-rule {
    width: 690px;
    height: 2px;
    background: var(--navy);
    margin: 6px 0 6px;
  }
  .holder-title {
    font-weight: 500;
    font-size: 20px;
    color: var(--ink);
  }

  .contact-block {
    position: absolute;
    left: 56px;
    top: 318px;
  }
  .contact-rule {
    width: 300px;
    height: 2px;
    background: var(--navy);
    margin-bottom: 14px;
  }
  .contact { list-style: none; }
  .contact li {
    display: flex;
    align-items: flex-start;
    gap: 12px;
    font-size: 18px;
    line-height: 24px;
    margin-bottom: 4px;
    color: var(--ink);
  }
  .contact svg { width: 20px; height: 20px; margin-top: 2px; flex: none; fill: var(--navy); }

  .back-circle {
    width: 210px;
    height: 210px;
    border-radius: 50%;
    background: var(--gold);
  }
  .back-name {
    font-weight: 700;
    font-size: 30px;
    letter-spacing: 2px;
    text-transform: uppercase;
    color: var(--paper);
  }
</style>
</head>
<body>

<section class="card card-front" aria-label="Business card front">
  <header class="brand">
    <div class="brand-name">Ledgerhouse of<br>Seagrove Shores</div>
    <div class="brand-tagline">Licensed CPA Firm</div>
  </header>

  <div class="holder">
    <div class="holder-name">Rosalind M. Vantrecourt</div>
    <div class="holder-rule"></div>
    <div class="holder-title">CPA</div>
  </div>

  <div class="contact-block">
    <div class="contact-rule"></div>
    <ul class="contact">
      <li>
        <svg viewBox="0 0 24 24" aria-hidden="true"><path d="M6.6 10.8a15.1 15.1 0 0 0 6.6 6.6l2.2-2.2a1 1 0 0 1 1-.25 11.4 11.4 0 0 0 3.6.57 1 1 0 0 1 1 1V20a1 1 0 0 1-1 1A17 17 0 0 1 3 4a1 1 0 0 1 1-1h3.5a1 1 0 0 1 1 1c0 1.25.2 2.45.57 3.6a1 1 0 0 1-.25 1z"/></svg>
        <span>(555) 748-2916</span>
      </li>
      <li>
        <svg viewBox="0 0 24 24" aria-hidden="true"><path d="M2 5h20v14H2z M2 5l10 8 10-8" fill="none" stroke="#22307f" stroke-width="2.2" stroke-linejoin="round"/></svg>
        <span>CPA@LedgerhouseofSeagroveShores.example</span>
      </li>
      <li>
        <svg viewBox="0 0 24 24" aria-hidden="true"><path d="M12 2a7 7 0 0 0-7 7c0 5.2 7 13 7 13s7-7.8 7-13a7 7 0 0 0-7-7zm0 9.5A2.5 2.5 0 1 1 12 6.5a2.5 2.5 0 0 1 0 5z"/></svg>
        <span>Servicing Seagrove Coast &amp; Beyond<br>North Seagrove Shores, SG 00417</span>
      </li>
    </ul>
  </div>
</section>

<section class="card card-back" aria-label="Business card back">
  <div class="back-circle"></div>
  <div class="back-name">Ledgerhouse of Seagrove Shores</div>
</section>

</body>
</html>
```